Permanent Makeup (cosmetics salon) Brochure

We need a 2-4 sites brochure for our Permanent Makeup (cosmetics salon). Our company is based in Austria / Vienna. -> Our homepage is www.mk-lorenzhuber.at
This brochure should show which treatments we provide ot our customers.

I've uploaded our old brochure, the content (text) would be nearly the same (look form "Must Haves", pics have to be new (look uploaded pics)
The old brochure is to dark. -> look for our homepage maybe you can make it like this

Target Market(s)

woman, age 25-70 years who wants to have permanent makeup on eyebrows, lips or eyeliner

Industry/Entity Type

Beauty Salon

Requirements
Must have
• pics which are uploaded.

*This text (somithing about our business)
"Für Frau Lorenzhuber ist Permanent Makeup ein Kunsthandwerk. Das Team von MK-Lorenzhuber ist spezialisiert auf natürliches Permanent Makeup damit der individuelle Typ jeder Kundin am schönsten zum Ausdruck kommt."

*We do this treatments: (english)
+ Augenbrauen Microblading (eyebrows)
+ Augenbrauen Permanent Makeup (eyebrows2)
+ Lidstrich Permanent Makeup (eyeliner)
+ Lip Blushing (lips)
+ Lippen Permanent Makeup (lips2)

* Our addresses (2 locations)
Wien
Kerngasse 7b/12, 1010 Wien
Tel: 01/5827316

Villach
Birkenhofweg 24, 9524 St. Ulrich
Tel: 0676/3158940

Mail: info@mk-lorenzhuber.at
www.mk-lorenzhuber.at

```html
<!DOCTYPE html>
<html lang="de">
<head>
<meta charset="utf-8">
<title>Marika Lorenzhuber – Permanent Makeup Flyer</title>
<link rel="stylesheet" href="https://fonts.googleapis.com/css2?family=Montserrat:wght@700&family=Open+Sans:wght@400;600&display=swap">
<style>
  :root {
    --backdrop: #f4f2ef;
    --beige: #cdb6a6;
    --beige-light: #e2d2c6;
    --gold: #e3c255;
    --gold-deep: #d6b040;
    --gold-light: #f8dd7c;
    --ink: #1a1a1a;
    --white: #ffffff;
  }
  * { margin: 0; padding: 0; box-sizing: border-box; }
  html, body { width: 1200px; height: 764px; overflow: hidden; background: var(--backdrop); }
  .canvas { position: relative; width: 1200px; height: 764px; }
  .flyer {
    position: absolute; left: 344px; top: 20px;
    width: 920px; height: 1300px;
    transform: scale(0.5565); transform-origin: top left;
    overflow: hidden; background: var(--beige);
    font-family: "Open Sans", sans-serif; color: var(--ink);
  }
  .flyer-bg { position: absolute; inset: 0; }
  .brand { position: absolute; left: 40px; top: 44px; display: flex; align-items: center; gap: 18px; }
  .brand-name { font-family: "Open Sans", sans-serif; font-weight: 600; font-size: 40px; color: var(--ink); }
  .brand-dot { width: 60px; height: 60px; border-radius: 50%; background: var(--gold-deep); }
  .tagline {
    position: absolute; left: 55px; top: 112px;
    font-family: "Open Sans", sans-serif; font-weight: 600; font-size: 13px; letter-spacing: 1.6px;
  }
  .intro {
    position: absolute; left: 55px; top: 306px; width: 400px;
    font-size: 20px; line-height: 26px; text-align: justify; letter-spacing: 0.5px;
  }
  .treatments-title {
    position: absolute; left: 55px; top: 556px;
    font-family: "Montserrat", sans-serif; font-weight: 700; font-size: 29px; letter-spacing: -0.5px;
  }
  .treatment { position: absolute; width: 260px; text-align: center; }
  .treatment-photo {
    width: 222px; height: 222px; margin: 0 auto; border-radius: 50%;
    border: 8px solid var(--white);
  }
  .treatment-label { font-size: 24px; line-height: 30px; margin-top: 6px; }
  .tone-brow { background: radial-gradient(circle at 40% 45%, #e9d3c6, #c79f86); }
  .tone-face { background: radial-gradient(circle at 45% 40%, #f1d8c8, #c99a7e); }
  .tone-eye { background: radial-gradient(circle at 50% 55%, #e6c7b2, #9a7260); }
  .tone-lip { background: radial-gradient(circle at 50% 55%, #e8938a, #d6a896); }
  .tone-lip2 { background: radial-gradient(circle at 50% 55%, #eea092, #e9c3b3); }
  .contact {
    position: absolute; left: 577px; top: 472px; width: 326px; height: 326px;
    border-radius: 50%; background: var(--white); padding: 16px;
  }
  .contact-inner {
    width: 100%; height: 100%; border-radius: 50%;
    background: linear-gradient(160deg, var(--gold-light), var(--gold-deep));
    display: flex; flex-direction: column; align-items: center; justify-content: center;
    font-size: 20px; line-height: 26px; text-align: center;
  }
  .contact-icons { display: flex; gap: 8px; margin-bottom: 14px; }
  .addresses-rule { position: absolute; left: 272px; top: 1228px; width: 374px; height: 3px; background: var(--ink); }
  .addresses-title {
    position: absolute; left: 0; width: 920px; top: 1236px; text-align: center;
    font-family: "Montserrat", sans-serif; font-weight: 700; font-size: 22px; padding-left: 0;
  }
  .addresses-line { position: absolute; left: 0; width: 920px; top: 1270px; text-align: center; font-size: 16px; padding-left: 0; }
  .addresses-line .sep { margin: 0 14px; }
</style>
</head>
<body>
<div class="canvas">
  <div class="flyer">
    <svg class="flyer-bg" width="920" height="1300" viewBox="0 0 920 1300">
      <defs>
        <linearGradient id="beigeGrad" x1="0" y1="0" x2="1" y2="0">
          <stop offset="0" stop-color="#cdb6a6"/><stop offset="1" stop-color="#dcc8ba"/>
        </linearGradient>
        <linearGradient id="goldGrad" x1="0" y1="0" x2="1" y2="0.3">
          <stop offset="0" stop-color="#dfbd4f"/><stop offset="0.75" stop-color="#e8c75c"/><stop offset="1" stop-color="#f9df80"/>
        </linearGradient>
        <linearGradient id="portraitGrad" x1="0" y1="0" x2="0" y2="1">
          <stop offset="0" stop-color="#3a2c28"/><stop offset="0.35" stop-color="#e2c3b1"/><stop offset="1" stop-color="#d7b6a2"/>
        </linearGradient>
      </defs>
      <rect width="920" height="1300" fill="url(#beigeGrad)"/>
      <rect x="470" y="0" width="450" height="700" fill="url(#portraitGrad)" opacity="0.55" role="img" aria-label="Porträtfoto einer Frau beim Auftragen von Lidschatten"/>
      <path d="M0,168 C170,150 330,210 440,320 C540,420 600,520 700,540 C790,560 860,600 920,620 L920,1300 L0,1300 Z" fill="url(#goldGrad)"/>
      <path d="M0,168 C170,150 330,210 440,320 C540,420 600,520 700,540" fill="none" stroke="#c9a640" stroke-width="6" opacity="0.6"/>
    </svg>

    <div class="brand"><span class="brand-name">Marika</span><span class="brand-dot"></span><span class="brand-name">Lorenzhuber</span></div>
    <div class="tagline">WAS IHNEN WERTVOLL IST, GEHÖRT IN GUTE HÄNDE</div>

    <p class="intro">Für Frau Lorenzhuber ist Permanent Makeup ein Kunsthandwerk. Das Team von MK-Lorenzhuber ist spezialisiert auf natürliches Permanent Makeup damit der individuelle Typ jeder Kundin am schönsten zum Ausdruck kommt</p>

    <h2 class="treatments-title">WE DO THIS TREATMENTS:</h2>

    <div class="treatment" style="left:36px;top:602px">
      <div class="treatment-photo tone-brow" role="img" aria-label="Nahaufnahme Augenbraue mit Microblading"></div>
      <div class="treatment-label">Augenbrauen<br>Microblading</div>
    </div>
    <div class="treatment" style="left:300px;top:602px">
      <div class="treatment-photo tone-face" role="img" aria-label="Gesicht mit Augenbrauen Permanent Makeup"></div>
      <div class="treatment-label">Augenbrauen<br>Permanent Makeup</div>
    </div>
    <div class="treatment" style="left:36px;top:907px">
      <div class="treatment-photo tone-eye" role="img" aria-label="Nahaufnahme Auge mit Lidstrich"></div>
      <div class="treatment-label">Lidstrich<br>Permanent Makeup</div>
    </div>
    <div class="treatment" style="left:300px;top:907px">
      <div class="treatment-photo tone-lip" role="img" aria-label="Nahaufnahme Lippen mit Lip Blushing"></div>
      <div class="treatment-label">Lip<br>Blushing</div>
    </div>
    <div class="treatment" style="left:562px;top:907px">
      <div class="treatment-photo tone-lip2" role="img" aria-label="Nahaufnahme Lippen mit Permanent Makeup"></div>
      <div class="treatment-label">Lippen<br>Permanent Makeup</div>
    </div>

    <div class="contact">
      <div class="contact-inner">
        <div class="contact-icons">
          <svg width="30" height="30" viewBox="0 0 30 30" aria-label="Telefon"><circle cx="15" cy="15" r="13" fill="none" stroke="#1a1a1a" stroke-width="2"/><path d="M10,8 l3,0 l1,4 l-2,1.5 c1,2.5 2.5,4 5,5 l1.5,-2 l4,1 l0,3 c-7,0 -12.5,-5.5 -12.5,-12.5z" fill="#1a1a1a"/></svg>
          <svg width="30" height="30" viewBox="0 0 30 30" aria-label="E-Mail"><circle cx="15" cy="15" r="13" fill="none" stroke="#1a1a1a" stroke-width="2"/><rect x="8" y="10" width="14" height="10" fill="#1a1a1a"/><path d="M8,10 l7,6 l7,-6" fill="none" stroke="#e3c255" stroke-width="1.5"/></svg>
          <svg width="30" height="30" viewBox="0 0 30 30" aria-label="Web"><circle cx="15" cy="15" r="13" fill="none" stroke="#1a1a1a" stroke-width="2"/><circle cx="15" cy="15" r="8" fill="none" stroke="#1a1a1a" stroke-width="1.5"/><ellipse cx="15" cy="15" rx="3.5" ry="8" fill="none" stroke="#1a1a1a" stroke-width="1.5"/><path d="M7,15 h16 M8.5,11 h13 M8.5,19 h13" stroke="#1a1a1a" stroke-width="1.2"/></svg>
        </div>
        <div>0676/3158940</div>
        <div>info@mk-lorenzhuber.at</div>
        <div>www.mk-lorenzhuber.at</div>
      </div>
    </div>

    <div class="addresses-rule"></div>
    <div class="addresses-title">OUR ADDRESSES</div>
    <div class="addresses-line">Wien, Kerngasse 7b/12, 1010 Wien<span class="sep">|</span>Villach, Birkenhofweg 24, 9524 St. Ulrich</div>
  </div>
</div>
</body>
</html>
```